Lena Corvell Business Card

I need a business card that reflects my current website: itslenacorvell.example and screenshot attached. If we keep the color scheme of the site and sample card below that would be ideal. The business card should include the information on the attached sample cards.

Industry/Entity Type

Business

```html
<!DOCTYPE html>
<html lang="en">
<head>
<meta charset="utf-8">
<title>Lena Corvell Business Card</title>
<link rel="stylesheet" href="https://fonts.googleapis.com/css2?family=Open+Sans:wght@300;400&display=swap">
<style>
  :root {
    --backdrop: #e9e8e8;
    --card: #f7f6f5;
    --ink: #3a3a3a;
    --ink-soft: #5a5a5a;
    --edge: #dcdad8;
  }
  * { margin: 0; padding: 0; box-sizing: border-box; }
  html, body {
    width: 1200px;
    height: 844px;
    overflow: hidden;
    background: var(--backdrop);
  }
  .sheet {
    position: relative;
    width: 1200px;
    height: 844px;
    display: flex;
    align-items: center;
    justify-content: center;
    gap: 40px;
    font-family: "Open Sans", sans-serif;
    color: var(--ink);
  }
  .card {
    width: 500px;
    height: 286px;
    background: var(--card);
    border: 1px solid var(--edge);
    position: relative;
  }
  .card-back {
    padding: 58px 0 0 44px;
  }
  .card-back .name {
    font-size: 30px;
    font-weight: 400;
    letter-spacing: 0.04em;
    text-transform: uppercase;
    line-height: 1.1;
    margin-bottom: 6px;
  }
  .card-back .detail {
    font-size: 14.5px;
    font-weight: 400;
    color: var(--ink-soft);
    line-height: 1.45;
  }
  .card-front {
    display: flex;
    align-items: center;
    justify-content: center;
  }
  .card-front .wordmark {
    font-size: 40px;
    font-weight: 300;
    color: var(--ink);
    letter-spacing: 0.01em;
  }
</style>
</head>
<body>
  <main class="sheet">
    <section class="card card-back" aria-label="Card back with contact details">
      <h1 class="name">Lena Corvell</h1>
      <p class="detail">me@lenacorvell.example</p>
      <p class="detail">555.014.2270</p>
      <p class="detail">Brand Curator | Digital Storyteller | Social Entrepreneur</p>
      <p class="detail">[fb] | [t] | [ig] @itslenacorvell</p>
      <p class="detail">www.itslenacorvell.example</p>
    </section>
    <section class="card card-front" aria-label="Card front with name">
      <p class="wordmark">Lena Corvell</p>
    </section>
  </main>
</body>
</html>
```